Keystone Habitat Australia Business Card

We need a Business Card design for our new start up company.
A unique model designed to address Australia’s growing housing affordability problem has been launched. More than half of Australians are being priced out of the property market and have resigned themselves to the fact that they may never be able to afford a home.
We have developed a unique Algorithm that allows people to get into property and reverse this trend of domination by the property investors in this country. The first of its kind model facilitates connecting people to lending facilities that do not require them to have the finance combined under the purchase contract.
Ownership is shared with a second-tier investor, made up of either family or friends if not, Keystone Habitat Australia will provide a mini property investor enabling thousands of people the opportunity to buy a home, which they otherwise thought was not possible.
Keystone Habitat Australia is addressing housing affordability for families and individuals, giving every Australian looking to buy a home the opportunity to enter the property market to live in or invest.
Under our unique model, there is no combined finance, and individuals are assessed for their percentage portion of the property only. “A unique feature of our product is it is based around the strategies used for property investment. I have developed a unique Algorithm that enables the Home buyer to purchase 60% of a property, while Keystone Habitat Australia facilitates a second-tier investor to buy the other 40%. The Algorithm locks the investor in place and enables the home buyer to stairway to full ownership. The investment is secured against real property.
Please refer to our website www.keystonehabitat.com.au for inspiration.
Also please find attached our logo.
Any further directions please ask.
Cheers Dean
Real Estate
Dean Marrow
CEO
Mobile 0400 617 290
www.keystonehabitat.com.au
Email: dean@keystonehabitat.com.au
Designer to choose colors to be used in the design.

```html
<!DOCTYPE html>
<html lang="en">
<head>
<meta charset="utf-8">
<title>Keystone Habitat Australia – Business Card</title>
<link href="https://fonts.googleapis.com/css2?family=Montserrat:wght@400;500;600;700;800&display=swap" rel="stylesheet">
<style>
  :root {
    --backdrop: #1c1c1e;
    --brand-green: #27a44f;
    --brand-cyan: #1bb3d8;
    --brand-blue: #2aa9d9;
    --ink: #3a3a3a;
    --ink-soft: #555;
    --paper: #ffffff;
  }
  * { box-sizing: border-box; margin: 0; padding: 0; }
  html, body {
    width: 1200px; height: 1000px; overflow: hidden;
    background: var(--backdrop);
    font-family: "Montserrat", sans-serif;
  }
  .stage { position: relative; width: 1200px; height: 1000px; }

  .card {
    position: absolute;
    width: 560px; height: 320px;
    border-radius: 26px;
    overflow: hidden;
  }

  /* Front */
  .card-front {
    left: 80px; top: 150px;
    background: linear-gradient(35deg, var(--brand-green) 0%, #22ad8a 50%, var(--brand-cyan) 100%);
    color: var(--paper);
    text-align: center;
  }
  .front-brand {
    position: absolute; left: 0; right: 0; top: 88px;
    display: flex; flex-direction: column; align-items: center;
  }
  .front-brand .brand-dot {
    width: 38px; height: 38px; border-radius: 50%;
    background: var(--paper);
    margin-bottom: 14px;
  }
  .front-brand .brand-name {
    font-weight: 800; font-size: 27px; letter-spacing: 0.2px;
  }
  .front-brand .tagline {
    font-weight: 500; font-size: 14px; margin-top: 4px;
  }
  .front-web {
    position: absolute; left: 0; right: 0; top: 252px;
    font-size: 14px; font-weight: 500;
  }

  /* Back */
  .card-back {
    left: 560px; top: 520px;
    background: var(--paper);
  }
  .back-brand {
    position: absolute; left: 34px; top: 150px; width: 250px;
    display: flex; align-items: center; gap: 14px;
  }
  .back-brand .brand-dot {
    flex: none; width: 54px; height: 54px; border-radius: 50%;
    background: var(--brand-green);
  }
  .back-brand .brand-name {
    font-weight: 800; font-size: 22px; line-height: 1.15;
    color: var(--brand-blue);
  }
  .person {
    position: absolute; left: 318px; top: 46px; width: 230px;
  }
  .person .name {
    font-weight: 800; font-size: 23px; color: var(--brand-green);
    letter-spacing: 0.3px; text-transform: uppercase;
  }
  .person .role {
    font-size: 14px; color: var(--ink); margin-top: 2px;
  }
  .address {
    font-size: 13px; color: var(--ink-soft); line-height: 1.35; margin-top: 24px;
  }
  .contacts {
    list-style: none; margin-top: 26px;
    font-size: 13.5px; color: var(--ink);
  }
  .contacts li {
    display: flex; align-items: center; gap: 9px; line-height: 1.5;
  }
  .contacts svg { width: 12px; height: 12px; flex: none; fill: var(--brand-green); }
  .contacts .accent { color: var(--brand-green); }
</style>
</head>
<body>
<main class="stage">

  <section class="card card-front" aria-label="Business card front">
    <div class="front-brand">
      <span class="brand-dot"></span>
      <div class="brand-name">Keystone Habitat Australia</div>
      <div class="tagline">Making Home Ownership Achievable</div>
    </div>
    <div class="front-web">www.keystonehabitat.com.au</div>
  </section>

  <section class="card card-back" aria-label="Business card back">
    <div class="back-brand">
      <span class="brand-dot"></span>
      <div class="brand-name">Keystone Habitat Australia</div>
    </div>

    <div class="person">
      <div class="name">Dean Marrow</div>
      <div class="role">Founder/CEO</div>
      <div class="address">Your Street Address,<br>Australia, 1234</div>
      <ul class="contacts">
        <li>
          <svg viewBox="0 0 24 24" aria-hidden="true"><path d="M6.6 10.8a15.1 15.1 0 0 0 6.6 6.6l2.2-2.2a1 1 0 0 1 1-.25 11.4 11.4 0 0 0 3.6.57 1 1 0 0 1 1 1V20a1 1 0 0 1-1 1A17 17 0 0 1 3 4a1 1 0 0 1 1-1h3.5a1 1 0 0 1 1 1c0 1.25.2 2.45.57 3.57a1 1 0 0 1-.25 1z"/></svg>
          0400617290
        </li>
        <li>
          <svg viewBox="0 0 24 24" aria-hidden="true"><path d="M2 5h20v14H2z M2 5l10 8 10-8" fill="none" stroke="currentColor"/><path d="M2 5h20v2l-10 7L2 7z"/><path d="M2 8l10 7 10-7v11H2z"/></svg>
          dean@keystonehabitat.com.au
        </li>
        <li>
          <svg viewBox="0 0 24 24" aria-hidden="true"><circle cx="12" cy="12" r="10"/></svg>
          <span>www.<span class="accent">keystonehabitat</span>.com.au</span>
        </li>
      </ul>
    </div>
  </section>

</main>
</body>
</html>
```